New management consulting website

I need a 4-5 page website that I can manage in WordPress on Hostlane.example for a new management consulting company. The website is www.torvik-example.com and the company name is Torvik Group LLC. The attached spec has an example of a draft site, layout and actual copy and includes company and contact information. I have more high-res images I can send.

Must include instruction/assistance loading the site to my WordPress dashboard.

Target Market(s)

Any business, especially SAAS

Industry/Entity Type

Consultant

Coding

Coded - Design and coding required

Number of Pages Required

4 page

Font styles to use
Sans Serif

Colors
0456a4

Requirements
Must have
• Modern and stylish

```html
<!DOCTYPE html>
<html lang="en">
<head>
<meta charset="utf-8">
<title>Torvik Consulting</title>
<link href="https://fonts.googleapis.com/css2?family=Exo+2:wght@500;600&family=Mulish:wght@400;600;700&display=swap" rel="stylesheet">
<style>
:root{
  --navy:#1f3f6e;
  --navy-deep:#1d3e6f;
  --ink:#1b1b1b;
  --body:#333a44;
  --band:#e9eaec;
  --white:#ffffff;
  --line:rgba(255,255,255,.25);
}
*{box-sizing:border-box;margin:0;padding:0}
html,body{width:1200px;height:3773px;overflow:hidden}
body{font-family:"Mulish",Arial,sans-serif;color:var(--body);background:var(--white);position:relative}
.abs{position:absolute}
.heading{font-family:"Exo 2",Arial,sans-serif;font-weight:600;color:var(--navy);letter-spacing:.5px}
.center{left:0;width:1200px;text-align:center}
.btn{position:absolute;display:flex;align-items:center;justify-content:center;background:var(--navy);color:var(--white);font-size:16px;border-radius:6px 0 6px 0;text-decoration:none}
.btn-outline{background:transparent;border:1.5px solid var(--white)}
p{line-height:24px;font-size:13.5px}

/* hero */
.hero{top:0;left:0;width:1200px;height:604px;background:linear-gradient(100deg,#f4f4f3 0%,#ecebe8 45%,#d9cfc0 70%,#c9b79d 100%)}
.brand{top:24px;left:161px;font-family:"Mulish",Arial,sans-serif;font-weight:700;font-size:34px;color:var(--navy);display:flex;align-items:center;gap:12px}
.brand-mark{width:22px;height:22px;border-radius:50%;background:var(--navy)}
.nav{top:42px;left:649px;display:flex;gap:31px;font-size:16px;color:var(--ink)}
.nav .active{color:var(--navy);font-weight:700}
.hero-title{top:261px;left:161px;height:149px;border-left:4px solid var(--navy);padding:10px 0 0 18px;font-size:31px;line-height:37px;color:var(--ink);font-weight:400}

/* services */
.services{top:980px;left:0;width:1200px;height:577px;background:var(--band)}
.card{position:absolute;top:205px;width:211px;height:281px;background:var(--white);border-radius:8px;text-align:center}
.card-icon{position:absolute;top:22px;left:62px;width:88px;height:88px;border-radius:50%;background:linear-gradient(#f3f5f9,#dfe4ec);box-shadow:0 3px 6px rgba(0,0,0,.15);display:flex;align-items:center;justify-content:center}
.card-title{position:absolute;top:130px;left:0;width:100%;font-weight:700;font-size:14px;color:var(--ink)}
.card-text{position:absolute;top:160px;left:14px;right:14px;font-size:13px;line-height:22px}
.card-link{position:absolute;top:244px;left:0;width:100%;font-size:14px;color:var(--ink);text-decoration:underline}

/* banner */
.banner{top:1944px;left:0;width:1200px;height:472px;background:linear-gradient(180deg,#2a4a78 0%,#50698c 45%,#3d5a82 70%,#1f3c69 100%)}

/* team */
.portrait{top:2574px;left:163px;width:383px;height:297px;background:linear-gradient(90deg,#cfd6de 0%,#e9edf1 40%,#f3f6f9 75%,#c5d0dc 100%)}

/* origins */
.gallery{top:3063px;height:205px;width:287px}

/* footer */
.footer{top:3359px;left:0;width:1200px;height:414px;background:var(--navy-deep);color:var(--white)}
.footer-brand{top:70px;left:0;width:100%;text-align:center;font-weight:700;font-size:36px;color:var(--white)}
.footer-nav{top:166px;left:0;width:100%;display:flex;justify-content:center;gap:51px;font-size:16px}
.rule{left:161px;width:878px;height:1px;background:var(--line)}
.contact{top:256px;display:flex;align-items:center;gap:14px;font-size:14px;line-height:19px}
.contact-icon{width:46px;height:46px;border-radius:50%;background:var(--white);display:flex;align-items:center;justify-content:center}
.contact small{font-size:12px}
.copyright{top:359px;left:163px;font-size:11px}
.social{top:354px;left:903px;display:flex;gap:8px}
.social span{width:28px;height:28px;border-radius:50%;background:var(--white)}
</style>
</head>
<body>

<!-- hero -->
<header class="abs hero" role="img" aria-label="Photo of a child in a pilot cap holding a toy plane in a bright room">
</header>
<div class="abs brand"><span>Torvik Consulting</span></div>
<nav class="abs nav"><span class="active">Home</span><span>About Us</span><span>Services</span></nav>
<a class="btn" style="left:910px;top:32px;width:129px;height:44px;">Contact Us</a>
<h1 class="abs hero-title">Our Approach Is To Help You<br>Rise Above Your Day-to-day<br>Business Challenges</h1>

<!-- intro -->
<h2 class="abs heading center" style="top:684px;font-size:39px;">ABOVE AND BEYOND</h2>
<p class="abs center" style="top:739px;font-weight:700;color:var(--ink);">The word ‘Torvik’ originates from old Northumbrian English language and means ‘above, beyond’.</p>
<p class="abs center" style="top:766px;">At Torvik Consulting our approach is to help you rise above your day-to-day business challenges, and build unique,<br>innovative solutions to move beyond them.</p>
<a class="btn" style="left:439px;top:847px;width:129px;height:42px;">Our Services</a>
<a class="btn" style="left:574px;top:847px;width:129px;height:42px;">About Us</a>

<!-- services -->
<section class="abs services">
  <h2 class="abs heading center" style="top:80px;font-size:39px;">OUR SERVICES</h2>
  <p class="abs" style="top:135px;left:175px;width:850px;text-align:center;color:var(--ink);">Lorem ipsum dolor sit amet, consectetuer adipiscing elit, sed diam nonummy nibh euismod tincidunt ut laoreet dlore magna aliquam erat volutpat. Ut wisifd fenim ad minim veniam, quis.</p>

  <div class="card" style="left:161px;">
    <div class="card-icon"><svg width="44" height="44" viewBox="0 0 44 44" fill="none" stroke="#1f3f6e" stroke-width="2"><circle cx="22" cy="22" r="14" stroke-dasharray="5 3"/><circle cx="22" cy="20" r="6"/><path d="M19 27h6M20 30h4"/></svg></div>
    <div class="card-title">Strategy &amp; Operations</div>
    <div class="card-text">Lorem ipsum dolor sit amet, consectetuer adipiscing elit, sed diam nonummy....</div>
    <div class="card-link">Read More</div>
  </div>
  <div class="card" style="left:384px;">
    <div class="card-icon"><svg width="44" height="44" viewBox="0 0 44 44" fill="none" stroke="#1f3f6e" stroke-width="2"><circle cx="19" cy="19" r="11"/><path d="M27 27l9 9"/><path d="M12 22l4-5 4 3 5-6"/></svg></div>
    <div class="card-title">Data Analysis &amp; Insights</div>
    <div class="card-text">Lorem ipsum dolor sit amet, consectetuer adipiscing elit, sed diam nonummy....</div>
    <div class="card-link">Read More</div>
  </div>
  <div class="card" style="left:605px;">
    <div class="card-icon"><svg width="44" height="44" viewBox="0 0 44 44" fill="none" stroke="#1f3f6e" stroke-width="2.5"><path d="M6 38h10v-8h10v-8h10v-8"/><path d="M26 8h10v10M36 8L24 20"/></svg></div>
    <div class="card-title">Leadership Development</div>
    <div class="card-text">Lorem ipsum dolor sit amet, consectetuer adipiscing elit, sed diam nonummy....</div>
    <div class="card-link">Read More</div>
  </div>
  <div class="card" style="left:828px;">
    <div class="card-icon"><svg width="44" height="44" viewBox="0 0 44 44" fill="#1f3f6e" stroke="#1f3f6e" stroke-width="2"><circle cx="22" cy="10" r="4"/><circle cx="9" cy="30" r="4"/><circle cx="22" cy="30" r="4"/><circle cx="35" cy="30" r="4"/><path d="M22 15v10M9 25v-4h26v4" fill="none"/></svg></div>
    <div class="card-title">Executive Leadership</div>
    <div class="card-text">Lorem ipsum dolor sit amet, consectetuer adipiscing elit, sed diam nonummy....</div>
    <div class="card-link">Read More</div>
  </div>
</section>

<!-- amazing -->
<h2 class="abs heading" style="top:1704px;left:163px;font-size:40px;line-height:45px;">AMAZING<br>THINGS FOR YOU</h2>
<p class="abs" style="top:1640px;left:551px;width:490px;">Lorem ipsum dolor sit amet, consectetuer adipiscing elit, sed diam nonummy nibh euismod tincidunt ut laoreet dlore magna aliquam erat volutpat. Ut wisifd fenim ad minim veniam, quis.</p>
<p class="abs" style="top:1720px;left:551px;width:490px;">Lorem ipsum dolor sit amet, consectetuer adipiscing elit, sed diam nonummy nibh euismod tincidunt ut laoreet dlore magna aliquam erat volutpat. Ut wisifd fenim ad minim veniam, quis.</p>
<a class="btn" style="left:543px;top:1811px;width:131px;height:42px;">Contact Us</a>

<!-- banner -->
<section class="abs banner" role="img" aria-label="Photo of two hikers raising their arms on a misty mountain ridge at dusk">
  <h3 class="abs center" style="top:154px;font-size:21px;font-weight:700;color:var(--white);">Lorem Ipsum Dolor Sit Amet, Consectetuer Adipiscing Elit</h3>
  <p class="abs center" style="top:194px;font-size:14px;line-height:26px;color:#e6ecf4;">Lorem Ipsum Dolor Sit Amet, Consectetuer Adipiscing Elit, Sed Diam Nonummy Nibh Euismod Tincidunt Ut<br>Laoreet Dlore Magna Aliquam Erat Volutpat. Ut Wisifd Fenim Ad Minim Veniam, Quis.</p>
  <a class="btn btn-outline" style="left:543px;top:267px;width:129px;height:42px;">Contact Us</a>
</section>

<!-- team -->
<h2 class="abs heading center" style="top:2497px;font-size:39px;">OUR TEAM</h2>
<div class="abs portrait" role="img" aria-label="Portrait photo of the founder standing by a bright window"></div>
<h3 class="abs heading" style="top:2587px;left:580px;font-size:26px;">Daniel Harrow</h3>
<div class="abs" style="top:2616px;left:582px;font-size:12px;font-weight:700;color:var(--navy);">Founder &amp; Senior Consultant</div>
<p class="abs" style="top:2640px;left:582px;width:460px;">Lorem ipsum dolor sit amet, consectetuer adipiscing elit, sed diam ummy nibh euismod tincidunt ut laoreet dlore magna aliquam erat volutpat. Ut wisifd fenim ad minim veniam, quis.</p>
<p class="abs" style="top:2719px;left:582px;width:460px;">Lorem ipsum dolor sit amet, consectetuer adipiscing elit, sed diam ummy nibh euismod tincidunt ut laoreet dlore magna aliquam erat volutpat. Ut wisifd fenim ad minim veniam, quis.</p>
<a class="btn" style="left:573px;top:2808px;width:130px;height:43px;">Contact Us</a>

<!-- origins -->
<h2 class="abs heading center" style="top:2956px;font-size:39px;">THE ORIGINS OF TORVIK</h2>
<p class="abs center" style="top:3014px;font-weight:700;color:var(--ink);">The word ‘Torvik’ originates from old Northumbrian English language and means ‘above, beyond’.</p>
<div class="abs gallery" style="left:161px;background:linear-gradient(180deg,#6d6fa0 0%,#e59a7a 30%,#7fb25a 60%,#3f7a2c 100%);" role="img" aria-label="Photo of green hills and a dry stone wall under a sunset sky"></div>
<div class="abs gallery" style="left:457px;background:linear-gradient(180deg,#8f9eb0 0%,#c9b49a 35%,#4d5a66 65%,#2f3a44 100%);" role="img" aria-label="Photo of a rocky coastline with waves at sunset"></div>
<div class="abs gallery" style="left:752px;background:linear-gradient(180deg,#dfe8ef 0%,#a9c0cf 30%,#8a8a4e 60%,#6e5b35 100%);" role="img" aria-label="Photo of a lone tree beside a stone path on a hillside"></div>

<!-- footer -->
<footer class="abs footer">
  <div class="abs footer-brand">Torvik Consulting</div>
  <nav class="abs footer-nav"><span>HOME</span><span>ABOUT US</span><span>SERVICES</span><span>CONTACT US</span></nav>
  <div class="abs rule" style="top:226px;"></div>
  <div class="abs contact" style="left:182px;">
    <div class="contact-icon"><svg width="22" height="22" viewBox="0 0 24 24" fill="none" stroke="#1f3f6e" stroke-width="1.8"><path d="M5 3h4l2 5-3 2a12 12 0 006 6l2-3 5 2v4a2 2 0 01-2 2A17 17 0 013 5a2 2 0 012-2z"/></svg></div>
    <div>PHONE<br>555.014.0199</div>
  </div>
  <div class="abs contact" style="left:474px;top:246px;">
    <div class="contact-icon"><svg width="22" height="22" viewBox="0 0 24 24" fill="none" stroke="#1f3f6e" stroke-width="1.8"><path d="M12 22s7-7 7-12a7 7 0 00-14 0c0 5 7 12 7 12z"/><circle cx="12" cy="10" r="2.5"/></svg></div>
    <div>ADDRESS<br><small>2210 Alder Row #410<br>Brookfield, GA 30000</small></div>
  </div>
  <div class="abs contact" style="left:845px;">
    <div class="contact-icon"><svg width="22" height="22" viewBox="0 0 24 24" fill="none" stroke="#1f3f6e" stroke-width="1.8"><rect x="3" y="6" width="18" height="13" rx="1.5"/><path d="M3 7l9 7 9-7"/></svg></div>
    <div>EMAIL<br>info@torvik-example.com</div>
  </div>
  <div class="abs rule" style="top:328px;"></div>
  <div class="abs copyright">COPYRIGHT © 2021 TORVIK CONSULTING. ALL RIGHTS RESERVED.</div>
  <div class="abs social" aria-label="Social links"><span></span><span></span><span></span><span></span></div>
</footer>

</body>
</html>
```